Gentleman's grooming products require a business card

I need a business card that incorporates the logo [ or parts of ] that we had Pixel Hive design for us as uploaded.

We sell online, mens grooming products including moustache waxes, beard oils and shaving accessories.
We want a card that is classy, professional and a card that shouts mens products.

Target Market(s)

Young professional male market

Industry/Entity Type

Business

Contact Information for Business Card

Ross and Edith Carwell
Lather and Lore
Purveyors of gentleman's stiffeners and grooming requisites
M :0418529647
E : ross@latherandlore.com.au
E : edith@latherandlore.com.au
E : sales@theblokesbalmery.com.au

W : www.latherandlore.com.au

Requirements
Must have
• Class
Nice to have
• Professionalism

```html
<!DOCTYPE html>
<html lang="en">
<head>
<meta charset="utf-8">
<title>Lather and Lore – Business Cards</title>
<link rel="stylesheet" href="https://fonts.googleapis.com/css2?family=Arimo:wght@400;700&display=swap">
<style>
  :root {
    --page: #e9e6e1;
    --card: #0b0b0b;
    --card-edge: #1c1c1c;
    --ink: #f4f4f4;
    --ink-soft: #cfcfcf;
    --rule: #bdbdbd;
    --edge-band: #8a8a8a;
  }
  * { box-sizing: border-box; margin: 0; padding: 0; }
  html, body { width: 1200px; height: 950px; overflow: hidden; }
  body {
    background: var(--page);
    font-family: "Arimo", Arial, sans-serif;
    color: var(--ink);
    display: flex;
    flex-direction: column;
    align-items: center;
    justify-content: center;
    gap: 34px;
  }
  .card {
    position: relative;
    width: 700px;
    height: 400px;
    background: linear-gradient(135deg, var(--card-edge) 0%, var(--card) 45%, var(--card) 100%);
    border-radius: 4px;
    box-shadow: 0 10px 24px rgba(0,0,0,0.25);
    overflow: hidden;
  }
  .brand {
    display: flex;
    flex-direction: column;
    align-items: center;
    gap: 10px;
  }
  .brand-rule {
    width: 100%;
    height: 1px;
    background: var(--rule);
  }
  .brand-line {
    display: flex;
    align-items: center;
    gap: 12px;
  }
  .brand-square {
    width: 18px;
    height: 18px;
    background: var(--ink);
  }
  .brand-name {
    font-size: 40px;
    font-weight: 400;
    color: var(--ink);
    letter-spacing: 0.5px;
    white-space: nowrap;
  }
  .brand-tagline {
    font-size: 9px;
    letter-spacing: 1.6px;
    text-transform: uppercase;
    color: var(--ink-soft);
    white-space: nowrap;
  }

  /* Front */
  .card-front {
    display: flex;
    flex-direction: column;
    align-items: center;
    justify-content: center;
    gap: 24px;
  }
  .front-web {
    font-size: 17px;
    font-weight: 700;
    letter-spacing: 3px;
  }

  /* Back */
  .card-back::before {
    content: "";
    position: absolute;
    left: 0; top: 0; bottom: 0;
    width: 16px;
    background: linear-gradient(90deg, var(--edge-band), #4a4a4a);
  }
  .card-back .brand {
    position: absolute;
    left: 56px;
    top: 200px;
    width: 330px;
  }
  .card-back .brand-name { font-size: 32px; }
  .card-back .brand-tagline { font-size: 6.5px; letter-spacing: 0.9px; }
  .contact {
    position: absolute;
    left: 420px;
    top: 120px;
    display: flex;
    flex-direction: column;
    gap: 9px;
  }
  .contact-name {
    font-size: 21px;
    font-weight: 700;
    margin-bottom: 6px;
    white-space: nowrap;
  }
  .contact-list { list-style: none; display: flex; flex-direction: column; gap: 7px; }
  .contact-item {
    display: flex;
    align-items: center;
    gap: 10px;
    font-size: 14px;
    color: var(--ink);
    white-space: nowrap;
  }
  .contact-icon { width: 15px; height: 15px; flex: none; }
</style>
</head>
<body>

  <section class="card card-front" aria-label="Business card front">
    <div class="brand">
      <span class="brand-rule"></span>
      <div class="brand-line">
        <span class="brand-square"></span>
        <span class="brand-name">Lather and Lore</span>
      </div>
      <span class="brand-rule"></span>
      <p class="brand-tagline">Makers of fine moustache waxes, beard oils and shaving goods</p>
    </div>
    <p class="front-web">www.latherandlore.com.au</p>
  </section>

  <section class="card card-back" aria-label="Business card back">
    <div class="brand">
      <span class="brand-rule"></span>
      <div class="brand-line">
        <span class="brand-square"></span>
        <span class="brand-name">Lather and Lore</span>
      </div>
      <span class="brand-rule"></span>
      <p class="brand-tagline">Makers of fine moustache waxes, beard oils and shaving goods</p>
    </div>

    <div class="contact">
      <p class="contact-name">Ross &amp; Edith Carwell</p>
      <ul class="contact-list">
        <li class="contact-item">
          <svg class="contact-icon" viewBox="0 0 16 16" aria-hidden="true"><rect x="4" y="1" width="8" height="14" rx="1.5" fill="none" stroke="#f4f4f4" stroke-width="1.5"/><circle cx="8" cy="12.5" r="0.9" fill="#f4f4f4"/></svg>
          0418529647
        </li>
        <li class="contact-item">
          <svg class="contact-icon" viewBox="0 0 16 16" aria-hidden="true"><rect x="1" y="3.5" width="14" height="9" fill="#f4f4f4"/><path d="M1 3.5 L8 9 L15 3.5" fill="none" stroke="#0b0b0b" stroke-width="1.2"/></svg>
          ross@latherandlore.com.au
        </li>
        <li class="contact-item">
          <svg class="contact-icon" viewBox="0 0 16 16" aria-hidden="true"><rect x="1" y="3.5" width="14" height="9" fill="#f4f4f4"/><path d="M1 3.5 L8 9 L15 3.5" fill="none" stroke="#0b0b0b" stroke-width="1.2"/></svg>
          edith@latherandlore.com.au
        </li>
        <li class="contact-item">
          <svg class="contact-icon" viewBox="0 0 16 16" aria-hidden="true"><rect x="1" y="3.5" width="14" height="9" fill="#f4f4f4"/><path d="M1 3.5 L8 9 L15 3.5" fill="none" stroke="#0b0b0b" stroke-width="1.2"/></svg>
          sales@theblokesbalmery.com.au
        </li>
        <li class="contact-item">
          <svg class="contact-icon" viewBox="0 0 16 16" aria-hidden="true"><circle cx="8" cy="8" r="7" fill="#f4f4f4"/><ellipse cx="8" cy="8" rx="3" ry="7" fill="none" stroke="#0b0b0b" stroke-width="1"/><line x1="1" y1="8" x2="15" y2="8" stroke="#0b0b0b" stroke-width="1"/></svg>
          www.latherandlore.com.au
        </li>
      </ul>
    </div>
  </section>

</body>
</html>
```